BRQ-Bramwell Resource Quarters LLC (Business Cards)

The attached design was selected as the logo for our company. I need to proceed on creating our business cards.

Tobias

Target Market(s)

This is a technology and Project Management company. The audience will be business decision makers of a diversity of companies.

Industry/Entity Type

Business

Font styles to use
Sans Serif
Script

Colors

Designer to choose colors to be used in the design.

```html
<!DOCTYPE html>
<html lang="en">
<head>
<meta charset="utf-8">
<title>Bramwell Resource Quarters – Business Card</title>
<link rel="stylesheet" href="https://fonts.googleapis.com/css2?family=Montserrat:wght@400&family=Source+Sans+3:wght@400;600&display=swap">
<style>
  :root {
    --page: #ffffff;
    --card: #f2f2c6;
    --ink: #2a2d30;
    --crimson: #951b27;
    --stripe-light: #ffffff;
  }
  html, body {
    margin: 0;
    padding: 0;
    width: 1200px;
    height: 1000px;
    overflow: hidden;
    background: var(--page);
  }
  .canvas {
    position: relative;
    width: 1200px;
    height: 1000px;
  }
  .card {
    position: absolute;
    left: 2px;
    top: 165px;
    width: 1196px;
    height: 685px;
    background: var(--card);
    overflow: hidden;
  }
  .stripes {
    position: absolute;
    left: 0;
    top: 0;
    width: 1196px;
    height: 685px;
  }
  .brand-mark {
    position: absolute;
    left: 61px;
    top: 435px;
    width: 230px;
    height: 230px;
    border-radius: 50%;
    background: var(--crimson);
  }
  .brand-name {
    position: absolute;
    left: 0;
    top: 0;
    width: 300px;
    margin: 0;
    transform-origin: top left;
    transform: translate(98px, 365px) rotate(-90deg);
    font-family: "Montserrat", sans-serif;
    font-weight: 400;
    font-size: 45px;
    line-height: 50px;
    color: var(--ink);
    white-space: nowrap;
  }
  .brand-name span { display: block; }
  .contact {
    position: absolute;
    right: 51px;
    margin: 0;
    text-align: right;
    font-family: "Source Sans 3", sans-serif;
    color: var(--ink);
    white-space: nowrap;
  }
  .contact-name {
    top: 281px;
    font-size: 32px;
    font-weight: 600;
    line-height: 40px;
  }
  .contact-role {
    top: 323px;
    font-size: 21px;
    line-height: 30px;
  }
  .contact-address,
  .contact-lines {
    font-size: 21px;
    line-height: 31px;
    font-style: normal;
  }
  .contact-address { top: 385px; }
  .contact-lines { top: 501px; }
  .contact-address span,
  .contact-lines span { display: block; }
</style>
</head>
<body>
<main class="canvas">
  <section class="card">
    <svg class="stripes" viewBox="0 0 1196 685" aria-hidden="true">
      <polygon points="818,0 856,0 666,685 650,685" fill="var(--stripe-light)"/>
      <polygon points="866,0 918,0 698,685 676,685" fill="var(--ink)"/>
      <polygon points="930,0 995,0 716,685 698,685" fill="var(--crimson)"/>
    </svg>

    <div class="brand-mark" aria-hidden="true"></div>
    <h1 class="brand-name">
      <span>Bramwell</span>
      <span>Resource</span>
      <span>Quarters</span>
    </h1>

    <p class="contact contact-name">Tobias Hale</p>
    <p class="contact contact-role">Managing Director</p>
    <address class="contact contact-address">
      <span>18 Larkfield Avenue</span>
      <span>California</span>
      <span>United States of America</span>
    </address>
    <p class="contact contact-lines">
      <span>tobias@bramwellrq.com</span>
      <span>+1 55 50 123 456</span>
    </p>
  </section>
</main>
</body>
</html>
```